2020 K FILM FESTIVAL CAMPAIGN

Theme: 20/20 Vision
"For the 2020 Brambleton Film Festival, we are looking at the vision of the festival as well as filmmaking. We are asking Designers to recreate an Eye Chart Test. The first row/letter (typically 'E') will be where the Logo goes, the second row will have 20 20 pay attention to the spacing between the '20s, the third row will have the letters BFF again note the spacing. These first three lines ideally are creating a pyramid. We are looking for a funky grime kind of font for "BFF & 2020". Instead of letters, we want to use symbols and the chart gets smaller in text. We the following symbols should be the largest on the chart a "Black Power Fist" "Female Symbol" Transgender Symbol" "recycling symbol". All over symbols should relate to Film and Cinema and the fine arts.

Font styles to use
Sans Serif
Decorative

Colors

Designer to choose colors to be used in the design.

Requirements
Nice to have
• Fancy fonts

```html
<!DOCTYPE html>
<html lang="en">
<head>
<meta charset="utf-8">
<title>2020 K Film Festival – Eye Chart</title>
<link rel="stylesheet" href="https://fonts.googleapis.com/css2?family=Alfa+Slab+One&display=swap">
<style>
  :root {
    --ink: #141414;
    --paper: #ffffff;
    --bar-red: #fb0102;
    --bar-green: #12a804;
  }
  html, body {
    margin: 0;
    padding: 0;
    overflow: hidden;
  }
  body {
    width: 1073px;
    height: 1200px;
    background: var(--paper);
    position: relative;
    font-family: "Alfa Slab One", Georgia, serif;
    color: var(--ink);
  }
  .festival-name {
    position: absolute;
    left: 0;
    top: 118px;
    width: 1073px;
    text-align: center;
    font-size: 26px;
    line-height: 1.2;
    color: var(--ink);
  }

  .chart-glyph {
    position: absolute;
    transform: translateX(-50%);
    line-height: 1;
    white-space: nowrap;
  }
  .row-year   { font-size: 100px; top: 254px; letter-spacing: -4px; }
  .row-brand  { font-size: 143px; top: 365px; }
  .row-three  { font-size: 126px; top: 513px; }
  .row-four   { font-size: 108px; top: 647px; }
  .row-five   { font-size: 44px;  top: 828px; }
  .row-six    { font-size: 39px;  top: 908px; }

  .rule {
    position: absolute;
    height: 27px;
  }
  .rule--red   { left: 187px; top: 777px; width: 706px; background: var(--bar-red); }
  .rule--green { left: 97px;  top: 980px; width: 886px; background: var(--bar-green); }

  .chart-icon {
    position: absolute;
    transform: translate(-50%, -50%);
    color: var(--ink);
  }
  .chart-icon--large { width: 44px; height: 44px; top: 1055px; }
  .chart-icon--small { width: 32px; height: 32px; top: 1053px; }
</style>
</head>
<body>

<svg width="0" height="0" style="position:absolute" aria-hidden="true">
  <defs>
    <symbol id="icon-target" viewBox="0 0 48 48">
      <circle cx="24" cy="24" r="17" fill="none" stroke="currentColor" stroke-width="3.5"/>
      <circle cx="24" cy="24" r="4" fill="none" stroke="currentColor" stroke-width="3"/>
      <path d="M24 1v9M24 38v9M1 24h9M38 24h9" stroke="currentColor" stroke-width="3"/>
    </symbol>
    <symbol id="icon-eye" viewBox="0 0 48 48">
      <path d="M2 12V4h7M46 36v8h-7" fill="none" stroke="currentColor" stroke-width="3"/>
      <path d="M6 24Q24 8 42 24Q24 40 6 24Z" fill="none" stroke="currentColor" stroke-width="3.5"/>
      <circle cx="24" cy="24" r="7" fill="none" stroke="currentColor" stroke-width="3"/>
      <circle cx="24" cy="24" r="2.5" fill="currentColor"/>
    </symbol>
    <symbol id="icon-star" viewBox="0 0 48 48">
      <path d="M3 12V3h9M36 3h9v9M45 36v9h-9M12 45H3v-9" fill="none" stroke="currentColor" stroke-width="3"/>
      <polygon points="24,11 28,20 38,21 30.5,28 33,38 24,33 15,38 17.5,28 10,21 20,20" fill="currentColor"/>
    </symbol>
    <symbol id="icon-check" viewBox="0 0 48 48">
      <circle cx="24" cy="24" r="19" fill="none" stroke="currentColor" stroke-width="4.5"/>
      <polyline points="14,24 21,31 34,17" fill="none" stroke="currentColor" stroke-width="5" stroke-linecap="round" stroke-linejoin="round"/>
    </symbol>
    <symbol id="icon-zoom" viewBox="0 0 48 48">
      <circle cx="19" cy="19" r="15" fill="none" stroke="currentColor" stroke-width="4"/>
      <path d="M19 11v16M11 19h16" stroke="currentColor" stroke-width="4.5"/>
      <path d="M30 30l14 14" stroke="currentColor" stroke-width="6" stroke-linecap="round"/>
    </symbol>
    <symbol id="icon-play" viewBox="0 0 48 48">
      <circle cx="24" cy="24" r="20" fill="none" stroke="currentColor" stroke-width="5"/>
      <polygon points="19,16 33,24 19,32" fill="currentColor"/>
    </symbol>
    <symbol id="icon-stage" viewBox="0 0 48 48">
      <path d="M4 6h22v16c0 10-5 16-11 16S4 32 4 22Z" fill="none" stroke="currentColor" stroke-width="3.5"/>
      <path d="M20 12h24v16c0 10-5 16-12 16s-12-6-12-16Z" fill="var(--paper)" stroke="currentColor" stroke-width="3.5"/>
    </symbol>
    <symbol id="icon-link" viewBox="0 0 48 48">
      <g transform="rotate(-45 24 24)" fill="none" stroke="currentColor" stroke-width="3.5">
        <rect x="2" y="18" width="24" height="12" rx="6"/>
        <rect x="22" y="18" width="24" height="12" rx="6"/>
      </g>
    </symbol>
  </defs>
</svg>

<div class="festival-name">Brambleton<br>Film Festival</div>

<span class="chart-glyph row-year" style="left:469px">20</span>
<span class="chart-glyph row-year" style="left:633px">20</span>

<span class="chart-glyph row-brand" style="left:368px">B</span>
<span class="chart-glyph row-brand" style="left:545px">F</span>
<span class="chart-glyph row-brand" style="left:717px">F</span>

<span class="chart-glyph row-three" style="left:301px">F</span>
<span class="chart-glyph row-three" style="left:474px">V</span>
<span class="chart-glyph row-three" style="left:647px">C</span>
<span class="chart-glyph row-three" style="left:794px">I</span>

<span class="chart-glyph row-four" style="left:245px">Z</span>
<span class="chart-glyph row-four" style="left:403px">M</span>
<span class="chart-glyph row-four" style="left:542px">G</span>
<span class="chart-glyph row-four" style="left:683px">N</span>
<span class="chart-glyph row-four" style="left:828px">R</span>

<div class="rule rule--red"></div>

<span class="chart-glyph row-five" style="left:173px">I</span>
<span class="chart-glyph row-five" style="left:240px">F</span>
<span class="chart-glyph row-five" style="left:307px">V</span>
<span class="chart-glyph row-five" style="left:373px">C</span>
<span class="chart-glyph row-five" style="left:442px">I</span>
<span class="chart-glyph row-five" style="left:506px">Z</span>
<span class="chart-glyph row-five" style="left:568px">I</span>
<span class="chart-glyph row-five" style="left:638px">F</span>
<span class="chart-glyph row-five" style="left:704px">V</span>
<span class="chart-glyph row-five" style="left:769px">C</span>
<span class="chart-glyph row-five" style="left:838px">I</span>
<span class="chart-glyph row-five" style="left:902px">Z</span>

<span class="chart-glyph row-six" style="left:142px">M</span>
<span class="chart-glyph row-six" style="left:198px">G</span>
<span class="chart-glyph row-six" style="left:256px">N</span>
<span class="chart-glyph row-six" style="left:319px">R</span>
<span class="chart-glyph row-six" style="left:374px">I</span>
<span class="chart-glyph row-six" style="left:438px">F</span>
<span class="chart-glyph row-six" style="left:499px">V</span>
<span class="chart-glyph row-six" style="left:580px">M</span>
<span class="chart-glyph row-six" style="left:638px">G</span>
<span class="chart-glyph row-six" style="left:696px">N</span>
<span class="chart-glyph row-six" style="left:759px">R</span>
<span class="chart-glyph row-six" style="left:814px">I</span>
<span class="chart-glyph row-six" style="left:878px">F</span>
<span class="chart-glyph row-six" style="left:940px">V</span>

<div class="rule rule--green"></div>

<svg class="chart-icon chart-icon--large" style="left:85px"><use href="#icon-target"/></svg>
<svg class="chart-icon chart-icon--large" style="left:150px"><use href="#icon-eye"/></svg>
<svg class="chart-icon chart-icon--large" style="left:216px"><use href="#icon-star"/></svg>
<svg class="chart-icon chart-icon--large" style="left:282px"><use href="#icon-check"/></svg>
<svg class="chart-icon chart-icon--large" style="left:347px"><use href="#icon-zoom"/></svg>
<svg class="chart-icon chart-icon--large" style="left:413px"><use href="#icon-play"/></svg>
<svg class="chart-icon chart-icon--large" style="left:479px"><use href="#icon-stage"/></svg>
<svg class="chart-icon chart-icon--large" style="left:544px"><use href="#icon-link"/></svg>
<svg class="chart-icon chart-icon--small" style="left:609px"><use href="#icon-zoom"/></svg>
<svg class="chart-icon chart-icon--small" style="left:669px"><use href="#icon-stage"/></svg>
<svg class="chart-icon chart-icon--small" style="left:722px"><use href="#icon-link"/></svg>
<svg class="chart-icon chart-icon--small" style="left:773px"><use href="#icon-play"/></svg>
<svg class="chart-icon chart-icon--small" style="left:828px"><use href="#icon-star"/></svg>
<svg class="chart-icon chart-icon--small" style="left:883px"><use href="#icon-target"/></svg>
<svg class="chart-icon chart-icon--small" style="left:939px"><use href="#icon-check"/></svg>
<svg class="chart-icon chart-icon--small" style="left:1001px"><use href="#icon-eye"/></svg>

</body>
</html>
```